Cedar Row Maintenance and Concierge Flyer

We need a flyer for cedar row maintenance and concierge service. We specialize in and provide residential maintenance and errand services to retired and semi retired persons living in the Lake Norman area. The services we include:
Lighting and plumbing repairs
Ceiling fan installation
Handicap accessories
Locks and security
Picture hanging
Hang blinds
Furniture arrangement / assembly
Pressure washing
Battery Jump start
and more...

Our Concierge services include:
Errand running
Grocery shopping
Wellness Checks
Dog Walk
Garbage Collection
and more...

We offer monthly service agreements and 24/7 access
Call text or e-mail for more information
704.555.0187
1cedarrowmaint@quillpostmail.com

The design should invoke a sense of trust and a customer service driven mission

Target Market(s)

Residential maintenance

Industry/Entity Type

Property Maintenance

Contact Information for Business Card

Derek Halvorsen
48176 Quimby Ferrel Rd.
Cornelius NC 28031
704.555.0187
with uploaded logo

Requirements
Nice to have
• Would like a postcard size flyer. Front and back
Should not have
• No pics of of people wearing hard hats or pics of blueprints. No pics of commercial or industrial maintenance.

```html
<!DOCTYPE html>
<html lang="en">
<head>
<meta charset="utf-8">
<title>Cedar Row Maintenance &amp; Concierge – Business Card</title>
<link rel="stylesheet" href="https://fonts.googleapis.com/css2?family=Source+Sans+3:ital,wght@0,400;0,600;0,700;1,700&display=swap">
<style>
  :root {
    --red: #d32028;
    --grey: #7c7c7c;
    --ink: #222222;
    --text: #2b2b2b;
    --paper: #ffffff;
    --backdrop: #1c1c1c;
  }
  * { box-sizing: border-box; margin: 0; padding: 0; }
  html, body { width: 1200px; height: 1200px; overflow: hidden; }
  body {
    background: var(--backdrop);
    font-family: "Source Sans 3", "Helvetica Neue", Arial, sans-serif;
    color: var(--text);
    position: relative;
  }
  .card {
    position: absolute;
    left: 272px;
    width: 656px;
    height: 393px;
    background: var(--paper);
    overflow: hidden;
  }
  .card--front { top: 170px; }
  .card--back  { top: 613px; }

  .brand { display: flex; align-items: center; gap: 14px; position: absolute; }
  .brand__dot { border-radius: 50%; background: var(--red); flex: none; }
  .brand__name { color: var(--grey); font-weight: 400; line-height: 1.05; }
  .brand__name span { display: block; }

  .card--front .brand { left: 150px; top: 96px; }
  .card--front .brand__dot { width: 60px; height: 60px; }
  .card--front .brand__title { font-size: 50px; letter-spacing: 0.5px; }
  .card--front .brand__sub { font-size: 19px; text-transform: uppercase; letter-spacing: 0.4px; margin-top: 4px; }

  .mission {
    position: absolute; left: 0; right: 0; top: 252px;
    text-align: center; font-size: 21px; line-height: 27px; color: var(--text);
  }
  .mission__lead { color: var(--red); font-weight: 700; }
  .mission__place { font-weight: 700; font-style: italic; color: var(--ink); }

  .card--back .brand { left: 58px; top: 48px; gap: 10px; }
  .card--back .brand__dot { width: 40px; height: 40px; }
  .card--back .brand__title { font-size: 32px; }
  .card--back .brand__sub { font-size: 12.5px; text-transform: uppercase; letter-spacing: 0.3px; margin-top: 3px; }

  .person { position: absolute; right: 54px; top: 54px; text-align: right; }
  .person__name { color: var(--red); font-weight: 700; font-size: 26px; line-height: 28px; }
  .person__role { font-size: 15px; color: var(--text); margin-top: 6px; }

  .offer {
    position: absolute; left: 0; right: 0; top: 166px;
    text-align: center; font-size: 18px; color: var(--text);
  }
  .services {
    position: absolute; left: 0; right: 0;
    display: flex; justify-content: center; gap: 18px;
  }
  .services--maintenance { top: 206px; }
  .services--concierge { top: 264px; gap: 16px; }
  .services svg { width: 30px; height: 30px; }
  .services--maintenance svg { fill: var(--red); stroke: var(--red); }
  .services--concierge svg { fill: var(--ink); stroke: var(--ink); width: 28px; height: 28px; }

  .contact-band {
    position: absolute; left: 0; right: 0; bottom: 0; height: 81px;
    background: var(--red); color: var(--paper);
    display: flex; align-items: center; justify-content: center; gap: 30px;
  }
  .contact { display: flex; align-items: center; gap: 12px; }
  .contact svg { width: 28px; height: 28px; }
  .contact__phone { font-weight: 700; font-size: 22px; letter-spacing: 0.3px; }
  .contact__email { font-size: 20px; }
</style>
</head>
<body>

<section class="card card--front" aria-label="Card front">
  <div class="brand">
    <span class="brand__dot"></span>
    <div class="brand__name">
      <span class="brand__title">Cedar Row</span>
      <span class="brand__sub">Maintenance &amp; Concierge</span>
    </div>
  </div>
  <p class="mission">
    <span class="mission__lead">WE SPECIALIZE</span> in and provide residential<br>
    maintenance and errand services to retired and semi<br>
    retired persons living in the <span class="mission__place">Lake Norman</span> area.
  </p>
</section>

<section class="card card--back" aria-label="Card back">
  <div class="brand">
    <span class="brand__dot"></span>
    <div class="brand__name">
      <span class="brand__title">Cedar Row</span>
      <span class="brand__sub">Maintenance &amp; Concierge</span>
    </div>
  </div>
  <div class="person">
    <p class="person__name">YOUR NAME</p>
    <p class="person__role">CEO, DIRECTOR</p>
  </div>

  <p class="offer">We offer monthly service agreements and 24/7 access</p>

  <div class="services services--maintenance">
    <!-- lighting and plumbing -->
    <svg viewBox="0 0 30 30" aria-label="Lighting and plumbing"><path d="M15 2a9 9 0 0 0-5 16.5V22h10v-3.5A9 9 0 0 0 15 2z" stroke="none"/><rect x="10" y="23" width="10" height="3" stroke="none"/><rect x="12" y="27" width="6" height="2" stroke="none"/></svg>
    <!-- ceiling fan -->
    <svg viewBox="0 0 30 30" aria-label="Ceiling fan"><circle cx="15" cy="15" r="3" stroke="none"/><path d="M15 13 L13 1 L17 1 Z M17 16 L28 22 L26 25 Z M13 16 L4 25 L2 22 Z" stroke="none"/></svg>
    <!-- accessibility -->
    <svg viewBox="0 0 30 30" aria-label="Handicap accessories"><circle cx="12" cy="4" r="3" stroke="none"/><path d="M12 8v10h9l3 8" fill="none" stroke-width="3"/><path d="M9 13a8 8 0 1 0 10 11" fill="none" stroke-width="2.5"/></svg>
    <!-- locks -->
    <svg viewBox="0 0 30 30" aria-label="Locks and security"><path d="M9 13V9a6 6 0 0 1 12 0v4" fill="none" stroke-width="3"/><rect x="6" y="13" width="18" height="15" rx="2" stroke="none"/><rect x="14" y="18" width="2" height="5" fill="#fff" stroke="none"/></svg>
    <!-- picture hanging -->
    <svg viewBox="0 0 30 30" aria-label="Picture hanging"><rect x="3" y="6" width="24" height="19" fill="none" stroke-width="2"/><path d="M7 22 Q15 8 23 22 Z" stroke="none"/></svg>
    <!-- blinds -->
    <svg viewBox="0 0 30 30" aria-label="Hang blinds"><rect x="1" y="3" width="28" height="4" stroke="none"/><rect x="4" y="7" width="22" height="20" stroke="none"/></svg>
    <!-- furniture -->
    <svg viewBox="0 0 30 30" aria-label="Furniture arrangement"><rect x="6" y="6" width="18" height="12" rx="3" stroke="none"/><rect x="2" y="12" width="6" height="12" rx="2" stroke="none"/><rect x="22" y="12" width="6" height="12" rx="2" stroke="none"/><rect x="6" y="18" width="18" height="6" stroke="none"/><rect x="4" y="24" width="3" height="3" stroke="none"/><rect x="23" y="24" width="3" height="3" stroke="none"/></svg>
    <!-- car -->
    <svg viewBox="0 0 30 30" aria-label="Pressure washing and jump start"><path d="M6 13l3-6h12l3 6z" stroke="none"/><rect x="2" y="13" width="26" height="9" rx="2" stroke="none"/><circle cx="8" cy="17" r="2" fill="#fff" stroke="none"/><circle cx="22" cy="17" r="2" fill="#fff" stroke="none"/><rect x="4" y="22" width="5" height="4" stroke="none"/><rect x="21" y="22" width="5" height="4" stroke="none"/></svg>
    <!-- and more -->
    <svg viewBox="0 0 30 30" aria-label="And more"><rect x="5" y="11" width="20" height="16" stroke="none"/><path d="M15 11 L22 2" fill="none" stroke-width="2"/></svg>
  </div>

  <div class="services services--concierge">
    <!-- errands -->
    <svg viewBox="0 0 30 30" aria-label="Errand running"><circle cx="19" cy="4" r="3" stroke="none"/><path d="M17 9 L12 17 L18 21 L15 28 M12 17 L5 24 M16 11 L23 15 M15 10 L9 11" fill="none" stroke-width="2.5" stroke-linecap="round"/></svg>
    <!-- groceries -->
    <svg viewBox="0 0 30 30" aria-label="Grocery shopping"><path d="M2 5h4l3 14h15l3-10H8" fill="none" stroke-width="2.5" stroke-linejoin="round"/><circle cx="11" cy="25" r="2.5" stroke="none"/><circle cx="22" cy="25" r="2.5" stroke="none"/></svg>
    <!-- wellness -->
    <svg viewBox="0 0 30 30" aria-label="Wellness checks"><path d="M8 3v8a5 5 0 0 0 10 0V3" fill="none" stroke-width="2"/><path d="M13 16v5a5 5 0 0 0 10 0v-4" fill="none" stroke-width="2"/><circle cx="23" cy="14" r="3" stroke="none"/></svg>
    <!-- pets -->
    <svg viewBox="0 0 30 30" aria-label="Dog walk"><ellipse cx="15" cy="21" rx="7" ry="6" stroke="none"/><ellipse cx="6" cy="13" rx="3" ry="4" stroke="none"/><ellipse cx="24" cy="13" rx="3" ry="4" stroke="none"/><ellipse cx="11" cy="6" rx="3" ry="4" stroke="none"/><ellipse cx="19" cy="6" rx="3" ry="4" stroke="none"/></svg>
    <!-- garbage -->
    <svg viewBox="0 0 30 30" aria-label="Garbage collection"><path d="M12 8 L15 3 L18 8 Q27 14 25 27 H5 Q3 14 12 8Z" stroke="none"/></svg>
  </div>

  <div class="contact-band">
    <div class="contact">
      <svg viewBox="0 0 28 28" aria-label="Phone"><rect x="2" y="2" width="24" height="24" rx="5" fill="#fff"/><path d="M10 7c-2 1-3 3-2 6 1 4 4 7 7 8 2 1 4 0 5-2l-3-3-2 1c-2-1-3-3-4-5l1-2z" fill="var(--red)"/></svg>
      <span class="contact__phone">704.555.0187</span>
    </div>
    <div class="contact">
      <svg viewBox="0 0 30 22" aria-label="Email" style="width:36px;height:26px"><rect x="1" y="1" width="28" height="20" fill="none" stroke="#fff" stroke-width="2"/><path d="M1 1 L15 12 L29 1 M1 21 L11 10 M29 21 L19 10" fill="none" stroke="#fff" stroke-width="2"/></svg>
      <span class="contact__email">1cedarrowmaint@quillpostmail.com</span>
    </div>
  </div>
</section>

</body>
</html>
```